Fish & Chip Shop Takeaway Packaging

We are opening a new Fish & Chop shop called Crumbo's and need urgent designs submitted for our takeaway packaging. Specifically:
1. Repetitive pattern for Butchers Paper (Each roll is 80cm tall and 200m long)
2. Takeaway Box with lid (245 x 95 x 85 mm)
3. Takeaway Paper Bag (290mm wide, 300mm high)
4. Napkin (175mm tall, 95mm wide)

I have attached our Crumbo's Logo. All packaging will be brown Kraft paper and or cardboard. One or two colours for printing is okay with those colours being either black, white and/or the crumbos logo colours.

I have also attached a document with some designs that we like. And a another document with packaging designs we have chosen in the past for our other shops (butchery and burger shop).

We are looking for really creative ideas that interact with our customers. Adding fun terminology or games/jokes, whilst keeping the time modern is what we are after.

Please don't hesitate to ask any questions.
Thanks Dana

Target Market(s)

Families

Requirements
Must have
• Crumbos Logo (colour or black and white)

```html
<!DOCTYPE html>
<html lang="en">
<head>
<meta charset="utf-8">
<title>Crumbo's Takeaway Paper Bag</title>
<link rel="stylesheet" href="https://fonts.googleapis.com/css2?family=Alfa+Slab+One&family=Anton&family=Archivo:wght@700&family=Bangers&family=Chivo:wght@900&family=Fira+Sans:wght@600&family=Kanit:ital,wght@1,700&family=Londrina+Solid:wght@900&family=Luckiest+Guy&family=Montserrat:wght@800&family=Open+Sans:wght@400;700&family=Oswald:wght@700&family=Passion+One&family=Permanent+Marker&family=Quicksand:wght@700&family=Righteous&family=Yesteryear&display=block">
<style>
  :root {
    --ink: #000000;
    --paper: #ffffff;
    --label-grey: #6f6f6f;
  }
  * { margin: 0; padding: 0; box-sizing: border-box; }
  html, body { width: 675px; height: 1200px; overflow: hidden; background: var(--paper); }
  .bag {
    position: relative;
    width: 675px;
    height: 1200px;
    background: var(--paper);
    color: var(--ink);
    overflow: hidden;
  }
  .bag-label {
    position: absolute;
    left: 0; right: 0; top: 12px;
    text-align: center;
    font: 400 14px "Open Sans", sans-serif;
    color: var(--label-grey);
  }
  .brand-badge {
    position: absolute;
    left: 153px; top: 57px;
    width: 366px; height: 366px;
  }
  .brand-name {
    position: absolute;
    left: 336px; top: 240px;
    transform: translate(-50%, -50%);
    font: 700 60px "Quicksand", sans-serif;
    color: var(--paper);
    white-space: nowrap;
  }
  .slang {
    position: absolute;
    white-space: nowrap;
    line-height: 1;
    color: var(--ink);
    transform: translate(-50%, -50%) rotate(var(--tilt, 0deg)) scale(var(--sx, 1), var(--sy, 1));
  }
  .knackered   { left: 159px; top: 468px; --tilt: 17deg;  font: italic 400 34px "Alfa Slab One", "Anton", sans-serif; }
  .spunk       { left: 536px; top: 447px; --tilt: -20deg; font: 400 58px "Luckiest Guy", "Bangers", sans-serif; }
  .bell        { left: 151px; top: 547px; --tilt: 5deg;   font: 400 46px "Passion One", "Anton", sans-serif; }
  .breakfast   { left: 489px; top: 531px; --tilt: -12deg; font: 400 56px "Yesteryear", cursive; }
  .flies       { left: 336px; top: 616px; --tilt: -3deg;  font: 400 38px "Alfa Slab One", "Anton", sans-serif; }
  .smugglers   { left: 139px; top: 675px; --tilt: 3deg;   font: 600 31px "Fira Sans", sans-serif; }
  .dead-horse  { left: 471px; top: 675px; --tilt: -5deg;  font: 400 43px "Bangers", "Anton", sans-serif; letter-spacing: 1px; }
  .cold-one    { left: 130px; top: 756px; --tilt: -10deg; --sy: 1.5; font: 400 38px "Anton", "Oswald", sans-serif; }
  .crow-eater  { left: 422px; top: 746px; --tilt: 5deg;   font: 400 50px "Anton", "Oswald", sans-serif; }
  .ankle-biter { left: 139px; top: 826px; --tilt: -4deg;  font: 700 42px "Archivo", sans-serif; }
  .tinnie      { left: 536px; top: 804px; --tilt: -10deg; font: 800 36px "Montserrat", sans-serif; }
  .sickie      { left: 478px; top: 861px; --tilt: 6deg;   font: 800 34px "Montserrat", sans-serif; }
  .gobsmacked  { left: 166px; top: 891px; --tilt: 3deg;   font: 400 40px "Righteous", sans-serif; }
  .trackie     { left: 499px; top: 918px;                 font: 700 28px "Oswald", "Anton", sans-serif; }
  .drongo      { left: 134px; top: 964px; --tilt: -13deg; font: 400 52px "Permanent Marker", "Bangers", sans-serif; }
  .banana      { left: 473px; top: 962px; --tilt: 6deg;   font: 700 45px "Quicksand", sans-serif; }
  .ciggie      { left: 203px; top: 1013px;                font: 900 38px "Chivo", sans-serif; }
  .frog        { left: 475px; top: 1031px; --tilt: 6deg;  font: 400 28px "Bangers", "Anton", sans-serif; letter-spacing: 1px; }
  .donkey      { left: 196px; top: 1066px; --tilt: -7deg; font: 900 46px "Londrina Solid", "Anton", sans-serif; }
  .chew        { left: 504px; top: 1092px;                font: 700 44px "Open Sans", sans-serif; }
  .dunny       { left: 148px; top: 1124px; --tilt: 7deg;  font: 400 43px "Bangers", "Anton", sans-serif; letter-spacing: 1px; }
  .flatout     { left: 487px; top: 1152px; --tilt: 8deg;  font: 400 26px "Bangers", "Anton", sans-serif; letter-spacing: 1px; }
  .five-finger { left: 182px; top: 1171px; --tilt: -2deg; font: italic 700 28px "Kanit", sans-serif; }
</style>
</head>
<body>
<main class="bag">
  <p class="bag-label">Takeaway Paper Bag</p>

  <svg class="brand-badge" viewBox="0 0 366 366" aria-hidden="true">
    <circle cx="183" cy="183" r="183" fill="var(--ink)"/>
  </svg>
  <p class="brand-name">Crumbo's</p>

  <p class="slang knackered">I'M KNACKERED</p>
  <p class="slang spunk">SPUNK</p>
  <p class="slang bell">Give me a bell</p>
  <p class="slang breakfast">Dogs Breakfast</p>
  <p class="slang flies">Drink with the flies</p>
  <p class="slang smugglers">Budgie Smugglers</p>
  <p class="slang dead-horse">DEAD HORSE DOGS EYE</p>
  <p class="slang cold-one">A COLD ONE</p>
  <p class="slang crow-eater">CROW EATER</p>
  <p class="slang ankle-biter">Ankle-biter</p>
  <p class="slang tinnie">Tinnie Time</p>
  <p class="slang sickie">Taking a Sickie</p>
  <p class="slang gobsmacked">Gobsmacked</p>
  <p class="slang trackie">TRACKIE DAKS</p>
  <p class="slang drongo">DRONGO</p>
  <p class="slang banana">Banana Bender</p>
  <p class="slang ciggie">Ciggie</p>
  <p class="slang frog">GO OFF LIKE A FROG IN A SOCK</p>
  <p class="slang donkey">Donkey's years</p>
  <p class="slang chew">Chew The Fat</p>
  <p class="slang dunny">DUNNY BUDGIE</p>
  <p class="slang flatout">FLATOUT LIKE A LIZARD DRINKING</p>
  <p class="slang five-finger">Five Finger Discount</p>
</main>
</body>
</html>
```